New Company Logo & Responsive Website Design for Codewell Harbor

Codewell Harbor provides a white labeled, digital lending platform technology solutions to the mortgage industry via a SaaS model. Our target market is Mortgage Companies and Banks who are looking for innovative technology to assist both borrowers and loan originators with the lending process, while automating as much of he process as possible.

Codewell Harbor is our company name, and our modular software offerings Include the following Products:

1) Applicant Harbor: A customizable, web based, point-of-sale application for borrowers to complete a loan application, and guide them through the mortgage process.

POS Definition
"A point of sale (POS) is the client-facing software solution that allows borrowers to create a customer portal, apply for a loan online, and seamlessly submit needed documentation."

2) Lending Harbor: A Mortgage Loan Origination System

LOS Definition
"A Mortgage Loan Origination System (LOS) is a platform that takes a completed loan application and facilitates the mortgage transaction from origination to post closing. LOS systems may include document management, pricing and eligibility engines, and compliance tools to decrease risk and increase loan manufacturing quality.

3) Dwelling Harbor: A brandable, home search website

The LOS and POS definitions provided above are just for your understanding of what these products are, not to be included word-for-word as website content.

We are looking for designs that are elegant, convey technical competency, simple to navigate, and set us apart from the competition.

We are not set on any particular colors at this point, so feel free to choose the best colors for your particular designs.

Please include company logo, both desktop and mobile designs with a template design for the website sub pages.

Some Examples of Mortgage Technology Websites offering similar products. These are to show the typical content, not designs that we particularly like or dislike.

https://quentrapo.com/
https://www.brivatokel.com/
https://www.dwarnomivex.com/
https://www.trelpanosky.com/
https://www.vondriquel.com/products/trail

Please send comments with additional questions.

Thank You For your participation.

Target Market(s)

Mortgage Companies

Number of Pages Required

2 page

```html
<!DOCTYPE html>
<html lang="en">
<head>
<meta charset="utf-8">
<title>Codewell Harbor — Mortgage software for the modern lender</title>
<link href="https://fonts.googleapis.com/css2?family=Lora:ital,wght@0,400;0,500;1,400&family=Nunito:ital,wght@0,400;0,600;0,700;1,400&display=swap" rel="stylesheet">
<style>
:root{
  --navy:#1f3b82;
  --navy-deep:#1a2f6e;
  --blue:#1b7fd6;
  --blue-soft:#e9f2fc;
  --orange:#f47a1f;
  --ink:#1f2a44;
  --muted:#5a6275;
  --line:#e6e9f0;
  --white:#ffffff;
  --violet:#7b6df0;
}
*{margin:0;padding:0;box-sizing:border-box}
html,body{width:1200px;height:4144px;overflow:hidden;background:var(--white)}
body{position:relative;font-family:"Nunito",sans-serif;color:var(--ink)}
.abs{position:absolute}
.serif{font-family:"Lora",serif;font-weight:400}
.btn{position:absolute;display:flex;align-items:center;justify-content:center;border-radius:16px;color:var(--white);font-size:10px;font-weight:700;box-shadow:0 4px 10px rgba(27,127,214,.25)}
.btn-blue{background:var(--blue)}
.btn-orange{background:var(--orange);box-shadow:0 4px 10px rgba(244,122,31,.3)}
.btn-navy{background:var(--navy)}
.brand{font-family:"Lora",serif;font-size:24px;color:var(--navy);display:flex;align-items:center;gap:8px}
.brand-dot{width:14px;height:14px;border-radius:50%;background:var(--orange)}
/* header */
.site-header{position:absolute;left:0;top:0;width:1200px;height:74px;background:var(--white)}
.main-nav a{position:absolute;top:30px;font-size:10px;font-weight:600;color:var(--ink);text-decoration:none}
.main-nav a.active{color:var(--blue)}
/* hero */
.hero{position:absolute;left:0;top:74px;width:1200px;height:382px;background:linear-gradient(100deg,#1f3d86 0%,#2a5bb0 55%,#3b78c7 100%)}
.hero-title{position:absolute;left:93px;top:110px;width:380px;font-size:28px;line-height:36px;color:var(--white)}
.mock{position:absolute;background:var(--white);border-radius:10px;box-shadow:0 8px 28px rgba(20,40,90,.18);overflow:hidden}
/* sections */
.eyebrow{position:absolute;left:0;width:1200px;text-align:center;font-size:10px;font-weight:700;color:var(--orange)}
.h2{position:absolute;left:0;width:1200px;text-align:center;font-size:27px;line-height:36px;color:var(--navy-deep)}
.lead{position:absolute;font-size:9.5px;line-height:17px;color:var(--muted);text-align:center}
.why-title{position:absolute;left:612px;top:852px;font-size:27px;color:var(--navy-deep)}
.why-item{position:absolute;left:612px;width:330px;height:60px}
.why-icon{position:absolute;left:0;top:0;width:48px;height:48px;border-radius:50%;background:var(--white);box-shadow:0 4px 14px rgba(20,40,90,.12);display:flex;align-items:center;justify-content:center}
.why-icon.on{background:var(--blue)}
.why-item h4{position:absolute;left:63px;top:2px;font-size:12px;font-weight:700;color:var(--ink)}
.why-item p{position:absolute;left:63px;top:20px;width:260px;font-size:9px;line-height:15px;color:var(--muted)}
.product-title{position:absolute;font-size:21px;color:var(--navy-deep)}
.product-title b{font-weight:500}
.product-sub{position:absolute;font-size:11px;font-weight:700;line-height:19px;color:var(--ink)}
.product-text{position:absolute;font-size:11px;line-height:19px;color:var(--muted)}
.shot{position:absolute;background:var(--white);border-radius:8px;box-shadow:0 6px 26px rgba(20,40,90,.12);overflow:hidden}
/* trusted */
.trusted{position:absolute;left:0;top:2398px;width:1200px;height:232px;background:var(--navy)}
.partner{position:absolute;top:140px;font-family:"Nunito",sans-serif;font-weight:700;font-size:14px;color:var(--white);display:flex;align-items:center;gap:8px;white-space:nowrap}
.partner i{display:block;width:18px;height:18px;background:var(--white);border-radius:2px}
/* testimonials */
.testimonials{position:absolute;left:0;top:2630px;width:1200px;height:620px;background:linear-gradient(180deg,#2d8cdb 0%,#2a86d6 60%,#7db7ea 100%)}
.quote{position:absolute;left:340px;top:160px;width:520px;text-align:center;font-size:14.5px;line-height:23px;font-style:italic;color:rgba(255,255,255,.85)}
/* news */
.news-card{position:absolute;top:3360px;width:250px;height:232px}
.news-img{position:absolute;left:0;top:0;width:250px;height:126px}
.news-box{position:absolute;left:18px;top:118px;width:214px;height:112px;background:var(--white);box-shadow:0 6px 20px rgba(20,40,90,.1);padding:30px 18px 0}
.news-box .date{font-size:8px;font-weight:700;color:var(--orange)}
.news-box h5{margin-top:6px;font-family:"Lora",serif;font-weight:400;font-size:11px;line-height:15px;color:var(--ink)}
.news-badge{position:absolute;left:18px;top:-8px;width:18px;height:18px;border-radius:50%;background:var(--orange)}
.cta{position:absolute;left:200px;top:3721px;width:800px;height:94px;background:linear-gradient(90deg,var(--navy) 0%,var(--blue) 100%);box-shadow:0 10px 26px rgba(27,80,170,.25)}
/* footer */
.foot-h{position:absolute;top:3870px;font-family:"Lora",serif;font-size:13px;color:var(--ink)}
.foot-list{position:absolute;top:3900px;list-style:none;font-size:9px;line-height:19px;color:var(--muted)}
.contact-line{position:absolute;left:406px;font-size:11px;color:var(--ink);display:flex;align-items:flex-start;gap:10px}
.social{position:absolute;left:968px;width:30px;height:30px;border-radius:50%;background:var(--navy)}
.copyright{position:absolute;left:0;top:4112px;width:1200px;text-align:center;font-size:8.5px;color:var(--muted)}
</style>
</head>
<body>

<!-- Header -->
<header class="site-header">
  <div class="abs brand" style="left:95px;top:22px"><span class="brand-dot"></span>Codewell Harbor</div>
  <nav class="main-nav">
    <a class="active" style="left:404px">Home</a>
    <a style="left:456px">About</a>
    <a style="left:510px">Products</a>
    <a style="left:578px">Why Us?</a>
    <a style="left:643px">News</a>
    <a style="left:693px">Partners</a>
    <a style="left:758px">Reviews</a>
    <a style="left:819px">Contact Us</a>
    <a style="left:937px;color:var(--blue)">Login</a>
  </nav>
  <div class="btn btn-blue" style="left:984px;top:21px;width:122px;height:32px;font-size:9.5px">Schedule a Demo</div>
</header>

<!-- Hero -->
<section class="hero" role="img" aria-label="Photo of hands working at a laptop under a deep blue tint">
  <h1 class="hero-title serif">Mortgage softwar and technology for the modern lender.</h1>
  <div class="btn btn-blue" style="left:93px;top:236px;width:100px;height:28px">Get Started</div>
</section>

<!-- Hero dashboard (desktop) -->
<div class="mock" style="left:668px;top:138px;width:438px;height:318px">
  <svg width="438" height="318" viewBox="0 0 438 318">
    <rect x="0" y="0" width="438" height="28" fill="#fff"/>
    <rect x="10" y="10" width="50" height="8" rx="2" fill="#c9d3e6"/>
    <rect x="300" y="10" width="60" height="8" rx="4" fill="#eef1f6"/>
    <circle cx="392" cy="14" r="6" fill="#c9d3e6"/>
    <rect x="0" y="28" width="70" height="290" fill="#f6f8fc"/>
    <rect x="10" y="40" width="50" height="9" rx="2" fill="var(--blue)"/>
    <rect x="10" y="58" width="40" height="5" rx="2" fill="#d6dce8"/>
    <rect x="10" y="70" width="36" height="5" rx="2" fill="#d6dce8"/>
    <rect x="80" y="40" width="78" height="30" rx="4" fill="#f4f6fa"/><circle cx="92" cy="55" r="6" fill="#4c8ef7"/>
    <rect x="166" y="40" width="78" height="30" rx="4" fill="#f4f6fa"/><circle cx="178" cy="55" r="6" fill="#41c4c4"/>
    <rect x="252" y="40" width="78" height="30" rx="4" fill="#f4f6fa"/><circle cx="264" cy="55" r="6" fill="#e06ad0"/>
    <rect x="338" y="40" width="90" height="30" rx="4" fill="#f4f6fa"/><circle cx="350" cy="55" r="6" fill="#f5a623"/>
    <rect x="80" y="80" width="210" height="100" rx="4" fill="#fafbfd"/>
    <path d="M90 160 C120 150 130 120 160 140 S200 170 220 130 S260 110 280 150" fill="none" stroke="#8fc6f5" stroke-width="2"/>
    <path d="M90 165 C120 160 140 140 170 150 S220 160 280 160" fill="none" stroke="#c8b8f2" stroke-width="1.5"/>
    <rect x="298" y="80" width="130" height="100" rx="4" fill="#fafbfd"/>
    <g fill="#3c8df0"><rect x="312" y="130" width="5" height="40"/><rect x="326" y="115" width="5" height="55"/><rect x="340" y="140" width="5" height="30"/><rect x="354" y="105" width="5" height="65"/><rect x="368" y="125" width="5" height="45"/><rect x="382" y="110" width="5" height="60"/><rect x="396" y="135" width="5" height="35"/><rect x="410" y="120" width="5" height="50"/></g>
    <rect x="80" y="190" width="150" height="110" rx="4" fill="#fafbfd"/>
    <circle cx="155" cy="242" r="26" fill="none" stroke="#e4e0fa" stroke-width="8"/>
    <circle cx="155" cy="242" r="26" fill="none" stroke="var(--violet)" stroke-width="8" stroke-dasharray="110 200"/>
    <rect x="238" y="190" width="190" height="80" rx="4" fill="#3d6fd0"/>
    <text x="250" y="222" font-family="Nunito,sans-serif" font-size="18" fill="#fff">12°</text>
    <rect x="238" y="274" width="190" height="26" fill="#f4f6fa"/>
  </svg>
</div>
<!-- Hero dashboard (phone) -->
<div class="mock" style="left:620px;top:240px;width:142px;height:288px;border-radius:16px">
  <svg width="142" height="288" viewBox="0 0 142 288">
    <text x="40" y="30" font-family="Lora,serif" font-size="8" fill="#1f3b82">Codewell Harbor</text>
    <rect x="10" y="44" width="38" height="34" rx="3" fill="#f4f6fa"/><rect x="52" y="44" width="38" height="34" rx="3" fill="#f4f6fa"/><rect x="94" y="44" width="38" height="34" rx="3" fill="#f4f6fa"/>
    <path d="M14 70 l8 -6 l8 4 l8 -8 l6 4" fill="none" stroke="#2ec27e" stroke-width="1.2"/>
    <path d="M56 70 l8 -4 l8 2 l8 -8 l6 6" fill="none" stroke="#2ec27e" stroke-width="1.2"/>
    <path d="M98 68 l8 -6 l8 6 l8 -4 l6 2" fill="none" stroke="#e0555b" stroke-width="1.2"/>
    <rect x="10" y="86" width="122" height="6" rx="2" fill="#e9edf4"/>
    <g fill="#eef1f6">
      <rect x="10" y="102" width="122" height="22" rx="3"/><rect x="10" y="128" width="122" height="22" rx="3"/>
      <rect x="10" y="154" width="122" height="22" rx="3"/><rect x="10" y="180" width="122" height="22" rx="3"/>
      <rect x="10" y="206" width="122" height="22" rx="3"/><rect x="10" y="232" width="122" height="22" rx="3"/>
    </g>
    <g fill="#f5a623"><circle cx="20" cy="113" r="5"/><circle cx="20" cy="139" r="5" fill="#e0555b"/><circle cx="20" cy="165" r="5" fill="#3c8df0"/><circle cx="20" cy="191" r="5" fill="#2b6cc4"/><circle cx="20" cy="217" r="5" fill="#2ec27e"/><circle cx="20" cy="243" r="5" fill="#7b6df0"/></g>
    <g font-family="Nunito,sans-serif" font-size="6" fill="#1f2a44"><text x="30" y="115">Alpha</text><text x="30" y="141">Beta</text><text x="30" y="167">Gamma</text><text x="30" y="193">Delta</text><text x="30" y="219">Sigma</text><text x="30" y="245">Omega</text></g>
    <g font-family="Nunito,sans-serif" font-size="6" fill="#1f2a44"><text x="104" y="115">$12,398</text><text x="104" y="141">$6,395</text><text x="104" y="167">$12,398</text><text x="104" y="193">$6,395</text><text x="104" y="219">$12,398</text><text x="104" y="245">$6,395</text></g>
    <circle cx="71" cy="274" r="7" fill="none" stroke="#dde2ea"/>
  </svg>
</div>

<!-- Intro -->
<p class="eyebrow" style="top:576px">Simple &nbsp;•&nbsp; Fully Automated &nbsp;•&nbsp; Profitable</p>
<h2 class="h2 serif" style="top:596px">Contrary to popular belief, lorem ipsum is not<br>simply random text.</h2>
<p class="lead" style="left:230px;top:690px;width:740px">Lorem Ipsum is simply dummy text of the printing and typesetting industry. Lorem Ipsum has been the industry's standard dummy text ever since the 1500s, when an unknown printer took a galley of type and scrambled it to make a type specimen book. It has survived not only five centuries, but also the leap into electronic typesetting, remaining essentially unchanged. It was popularised in the 1960s with the release ...</p>
<div class="btn btn-orange" style="left:550px;top:755px;width:100px;height:30px">About Us</div>

<!-- Why -->
<div class="mock" style="left:-10px;top:873px;width:522px;height:362px;border-radius:18px">
  <svg width="522" height="362" viewBox="0 0 522 362">
    <rect x="40" y="14" width="430" height="330" rx="4" fill="#fff" stroke="#eef1f6"/>
    <text x="50" y="48" font-family="Nunito,sans-serif" font-weight="700" font-size="9" fill="#1f2a44">PERFORMANCE</text>
    <text x="300" y="48" font-family="Nunito,sans-serif" font-size="7" fill="#5a6275">2017</text>
    <g font-family="Nunito,sans-serif" font-size="6" fill="#5a6275"><text x="100" y="74" fill="#1b7fd6">Products</text><text x="140" y="74">Orders</text><text x="174" y="74">Countries</text><text x="214" y="74">Others</text></g>
    <g fill="#f1f3f7"><rect x="50" y="92" width="270" height="1"/><rect x="50" y="118" width="270" height="1"/><rect x="50" y="144" width="270" height="1"/><rect x="50" y="170" width="270" height="1"/><rect x="50" y="196" width="270" height="1"/><rect x="50" y="222" width="270" height="1"/><rect x="50" y="248" width="270" height="1"/><rect x="50" y="274" width="270" height="1"/></g>
    <g fill="#d6dce8"><rect x="50" y="104" width="30" height="4"/><rect x="160" y="104" width="36" height="4"/><rect x="160" y="130" width="36" height="4"/><rect x="160" y="156" width="36" height="4"/><rect x="160" y="182" width="36" height="4"/><rect x="160" y="208" width="36" height="4"/><rect x="160" y="234" width="36" height="4"/><rect x="160" y="260" width="36" height="4"/></g>
    <g stroke="#f38b9b" fill="none"><path d="M300 106 l6 3 l6 -2"/><path d="M300 132 l6 3 l6 -2"/><path d="M300 158 l6 3 l6 -2"/><path d="M300 184 l6 3 l6 -2"/><path d="M300 210 l6 3 l6 -2"/><path d="M300 236 l6 3 l6 -2"/></g>
    <rect x="282" y="296" width="50" height="14" rx="3" fill="#7b6df0"/>
    <rect x="338" y="14" width="132" height="330" fill="#fbfcfe"/>
    <circle cx="404" cy="100" r="26" fill="none" stroke="#f7c9a5" stroke-width="3" stroke-dasharray="4 3"/>
    <text x="390" y="104" font-family="Nunito,sans-serif" font-weight="700" font-size="11" fill="#f47a1f">37.5%</text>
    <path d="M350 250 c10 -40 20 40 30 0 s20 -30 30 10" fill="none" stroke="#f47a1f" stroke-width="1.5"/>
  </svg>
</div>
<div class="mock" style="left:414px;top:998px;width:154px;height:217px;border-radius:14px">
  <svg width="154" height="217" viewBox="0 0 154 217">
    <text x="36" y="50" font-family="Lora,serif" font-size="9" fill="#1f3b82">Codewell Harbor</text>
    <text x="44" y="86" font-family="Nunito,sans-serif" font-weight="700" font-size="9" fill="#1f2a44">My Dashboard</text>
    <path d="M60 140 C80 130 110 118 140 114 L140 210 L60 210 Z" fill="#f15ab0"/>
    <path d="M60 130 C80 122 110 110 140 106 L140 114 C110 118 80 130 60 140 Z" fill="#f9c4e2"/>
  </svg>
</div>

<h2 class="why-title serif">Why Codewell Harbor</h2>
<p class="abs" style="left:612px;top:900px;width:330px;font-size:9px;line-height:15px;color:var(--muted)">Duis aute irure dolor in reprehenderit in voluptate velit esse cillum dolore eu fugiat nulla pariatur.</p>

<div class="why-item" style="top:955px">
  <div class="why-icon"><svg width="18" height="18" viewBox="0 0 18 18"><circle cx="9" cy="9" r="4" fill="none" stroke="#1b7fd6" stroke-width="1.6"/><circle cx="9" cy="9" r="7.5" fill="none" stroke="#1b7fd6" stroke-width="1.2" stroke-dasharray="3 2"/></svg></div>
  <h4>Sed do eiusmod tempor</h4><p>Excepteur sint occaecat cupidatat proident, sunt in culpa qui officia deserunt ...</p>
</div>
<div class="why-item" style="top:1022px">
  <div class="why-icon on"><svg width="18" height="18" viewBox="0 0 18 18"><circle cx="9" cy="6" r="3.5" fill="none" stroke="#fff" stroke-width="1.5"/><path d="M3 16 c0 -4 12 -4 12 0" fill="none" stroke="#fff" stroke-width="1.5"/></svg></div>
  <h4>Sed do eiusmod tempor</h4><p>Excepteur sint occaecat cupidatat proident, sunt in culpa qui officia deserunt ...</p>
</div>
<div class="why-item" style="top:1091px">
  <div class="why-icon"><svg width="18" height="18" viewBox="0 0 18 18"><text x="6" y="9" font-family="Nunito,sans-serif" font-size="9" fill="#1b7fd6">$</text><path d="M2 14 h10 l4 -3" fill="none" stroke="#1b7fd6" stroke-width="1.5"/></svg></div>
  <h4>Sed do eiusmod tempor</h4><p>Excepteur sint occaecat cupidatat proident, sunt in culpa qui officia deserunt ...</p>
</div>
<div class="why-item" style="top:1160px">
  <div class="why-icon"><svg width="18" height="18" viewBox="0 0 18 18"><path d="M3 11 v-2 a6 6 0 0 1 12 0 v2" fill="none" stroke="#1b7fd6" stroke-width="1.5"/><rect x="2" y="10" width="3" height="5" rx="1" fill="#1b7fd6"/><rect x="13" y="10" width="3" height="5" rx="1" fill="#1b7fd6"/></svg></div>
  <h4>Sed do eiusmod tempor</h4><p>Excepteur sint occaecat cupidatat proident, sunt in culpa qui officia deserunt ...</p>
</div>
<div class="btn btn-blue" style="left:612px;top:1242px;width:113px;height:30px">Get Started</div>

<!-- Products -->
<h2 class="h2 serif" style="top:1328px">Our products</h2>
<p class="lead" style="left:270px;top:1374px;width:660px;font-size:10.5px;line-height:19px">Lorem Ipsum is simply dummy text of the printing and typesetting industry. Lorem Ipsum has been the industry's standard dummy text ever since the 1500s, when an unknown</p>

<h3 class="product-title serif" style="left:200px;top:1487px">Applicant <b>Harbor</b></h3>
<p class="product-sub" style="left:200px;top:1530px;width:390px">A customizable, web based, point-of-sale application for borrowers to complete a loan application, and guide them through the mortgage process.</p>
<p class="product-text" style="left:200px;top:1607px;width:390px">"A point of sale (POS) is the client-facing software solution that allows borrowers to create a customer portal ...</p>
<div class="btn btn-blue" style="left:200px;top:1664px;width:112px;height:30px">Explore More</div>

<div class="shot" style="left:722px;top:1472px;width:384px;height:245px">
  <svg width="384" height="245" viewBox="0 0 384 245">
    <rect x="0" y="0" width="384" height="22" fill="#fff"/><text x="28" y="14" font-family="Lora,serif" font-size="6" fill="#1f3b82">Codewell Harbor</text>
    <rect x="0" y="22" width="60" height="223" fill="#fbfcfe"/>
    <g fill="#dbe0ea"><rect x="10" y="34" width="36" height="3"/><rect x="10" y="46" width="30" height="3"/><rect x="10" y="58" width="34" height="3"/><rect x="10" y="70" width="28" height="3"/><rect x="10" y="82" width="32" height="3"/><rect x="10" y="94" width="30" height="3"/><rect x="10" y="106" width="34" height="3"/><rect x="10" y="118" width="26" height="3"/><rect x="10" y="130" width="32" height="3"/></g>
    <rect x="70" y="30" width="304" height="8" fill="#ece9fb"/>
    <rect x="70" y="46" width="94" height="36" rx="3" fill="#f7f8fc"/><circle cx="150" cy="64" r="8" fill="none" stroke="#3c8df0" stroke-width="2"/>
    <rect x="172" y="46" width="94" height="36" rx="3" fill="#f7f8fc"/><circle cx="252" cy="64" r="8" fill="none" stroke="#e0555b" stroke-width="2"/>
    <rect x="274" y="46" width="100" height="36" rx="3" fill="#f7f8fc"/><circle cx="360" cy="64" r="8" fill="none" stroke="#f5a623" stroke-width="2"/>
    <path d="M80 150 C95 130 105 150 120 140 S140 125 160 145 S190 130 210 140 S240 125 260 140 S300 110 330 130 L350 120 L350 160 L80 160 Z" fill="#e4e0fb"/>
    <path d="M80 150 C95 130 105 150 120 140 S140 125 160 145 S190 130 210 140 S240 125 260 140 S300 110 330 130 L350 120" fill="none" stroke="#8d80f2" stroke-width="1.5"/>
    <rect x="70" y="176" width="80" height="60" rx="3" fill="#fafbfd"/>
    <circle cx="98" cy="216" r="14" fill="none" stroke="#f5a623" stroke-width="6" stroke-dasharray="40 90"/>
    <circle cx="98" cy="216" r="14" fill="none" stroke="#3c8df0" stroke-width="6" stroke-dasharray="30 90" stroke-dashoffset="-40"/>
    <rect x="160" y="176" width="120" height="60" rx="3" fill="#fafbfd"/>
    <rect x="290" y="176" width="84" height="60" rx="3" fill="#7b6df0"/>
  </svg>
</div>

<div class="shot" style="left:95px;top:1780px;width:384px;height:245px">
  <svg width="384" height="245" viewBox="0 0 384 245">
    <rect x="0" y="0" width="384" height="22" fill="#fff"/><text x="28" y="14" font-family="Lora,serif" font-size="6" fill="#1f3b82">Codewell Harbor</text>
    <rect x="0" y="22" width="60" height="223" fill="#fbfcfe"/>
    <g fill="#dbe0ea"><rect x="10" y="34" width="36" height="3"/><rect x="10" y="46" width="30" height="3"/><rect x="10" y="58" width="34" height="3"/><rect x="10" y="70" width="28" height="3"/><rect x="10" y="82" width="32" height="3"/><rect x="10" y="94" width="30" height="3"/><rect x="10" y="106" width="34" height="3"/><rect x="10" y="118" width="26" height="3"/><rect x="10" y="130" width="32" height="3"/></g>
    <rect x="70" y="30" width="304" height="8" fill="#ece9fb"/>
    <rect x="70" y="46" width="94" height="36" rx="3" fill="#f7f8fc"/><circle cx="150" cy="64" r="8" fill="none" stroke="#3c8df0" stroke-width="2"/>
    <rect x="172" y="46" width="94" height="36" rx="3" fill="#f7f8fc"/><circle cx="252" cy="64" r="8" fill="none" stroke="#e0555b" stroke-width="2"/>
    <rect x="274" y="46" width="100" height="36" rx="3" fill="#f7f8fc"/><circle cx="360" cy="64" r="8" fill="none" stroke="#f5a623" stroke-width="2"/>
    <path d="M80 150 C95 130 105 150 120 140 S140 125 160 145 S190 130 210 140 S240 125 260 140 S300 110 330 130 L350 120 L350 160 L80 160 Z" fill="#e4e0fb"/>
    <path d="M80 150 C95 130 105 150 120 140 S140 125 160 145 S190 130 210 140 S240 125 260 140 S300 110 330 130 L350 120" fill="none" stroke="#8d80f2" stroke-width="1.5"/>
    <rect x="70" y="176" width="80" height="60" rx="3" fill="#fafbfd"/>
    <circle cx="98" cy="216" r="14" fill="none" stroke="#f5a623" stroke-width="6" stroke-dasharray="40 90"/>
    <circle cx="98" cy="216" r="14" fill="none" stroke="#3c8df0" stroke-width="6" stroke-dasharray="30 90" stroke-dashoffset="-40"/>
    <rect x="160" y="176" width="120" height="60" rx="3" fill="#fafbfd"/>
    <rect x="290" y="176" width="84" height="60" rx="3" fill="#7b6df0"/>
  </svg>
</div>
<h3 class="product-title serif" style="left:612px;top:1796px">Lending <b>Harbor</b></h3>
<p class="product-sub" style="left:612px;top:1841px;width:390px">A Mortgage Loan Origination System</p>
<p class="product-text" style="left:612px;top:1877px;width:390px">"A Mortgage Loan Origination System (LOS) is a platform that takes a completed loan application and facilitates the mortgage transaction from origination to post closing. LOS systems may include document management, pricing and eligibility ...</p>
<div class="btn btn-orange" style="left:612px;top:1973px;width:113px;height:30px">Explore More</div>

<h3 class="product-title serif" style="left:200px;top:2105px">Dwelling <b>Harbor</b></h3>
<p class="product-sub" style="left:200px;top:2148px;width:390px">A Brandable, Home Search Website</p>
<p class="product-text" style="left:200px;top:2185px;width:370px">Lorem ipsum dolor sit amet, consectetur adipiscing elit, sed do eiusmod tempor incididunt ut labore et dolore magna aliqua. Ut enim ad minim veniam, quis nostrud exercitation ullamco laboris nisi ut aliquip commodo ...</p>
<div class="btn btn-blue" style="left:200px;top:2282px;width:112px;height:30px">Explore More</div>

<div class="shot" style="left:722px;top:2088px;width:384px;height:245px">
  <svg width="384" height="245" viewBox="0 0 384 245">
    <rect x="0" y="0" width="384" height="22" fill="#fff"/><text x="28" y="14" font-family="Lora,serif" font-size="6" fill="#1f3b82">Codewell Harbor</text>
    <rect x="0" y="22" width="60" height="223" fill="#fbfcfe"/>
    <g fill="#dbe0ea"><rect x="10" y="34" width="36" height="3"/><rect x="10" y="46" width="30" height="3"/><rect x="10" y="58" width="34" height="3"/><rect x="10" y="70" width="28" height="3"/><rect x="10" y="82" width="32" height="3"/><rect x="10" y="94" width="30" height="3"/><rect x="10" y="106" width="34" height="3"/><rect x="10" y="118" width="26" height="3"/><rect x="10" y="130" width="32" height="3"/></g>
    <rect x="70" y="30" width="304" height="8" fill="#ece9fb"/>
    <rect x="70" y="46" width="94" height="36" rx="3" fill="#f7f8fc"/><circle cx="150" cy="64" r="8" fill="none" stroke="#3c8df0" stroke-width="2"/>
    <rect x="172" y="46" width="94" height="36" rx="3" fill="#f7f8fc"/><circle cx="252" cy="64" r="8" fill="none" stroke="#e0555b" stroke-width="2"/>
    <rect x="274" y="46" width="100" height="36" rx="3" fill="#f7f8fc"/><circle cx="360" cy="64" r="8" fill="none" stroke="#f5a623" stroke-width="2"/>
    <path d="M80 150 C95 130 105 150 120 140 S140 125 160 145 S190 130 210 140 S240 125 260 140 S300 110 330 130 L350 120 L350 160 L80 160 Z" fill="#e4e0fb"/>
    <path d="M80 150 C95 130 105 150 120 140 S140 125 160 145 S190 130 210 140 S240 125 260 140 S300 110 330 130 L350 120" fill="none" stroke="#8d80f2" stroke-width="1.5"/>
    <rect x="70" y="176" width="80" height="60" rx="3" fill="#fafbfd"/>
    <circle cx="98" cy="216" r="14" fill="none" stroke="#f5a623" stroke-width="6" stroke-dasharray="40 90"/>
    <circle cx="98" cy="216" r="14" fill="none" stroke="#3c8df0" stroke-width="6" stroke-dasharray="30 90" stroke-dashoffset="-40"/>
    <rect x="160" y="176" width="120" height="60" rx="3" fill="#fafbfd"/>
    <rect x="290" y="176" width="84" height="60" rx="3" fill="#7b6df0"/>
  </svg>
</div>

<!-- Trusted by -->
<section class="trusted">
  <h2 class="h2 serif" style="top:42px;color:var(--white)">Trusted by 47,000+ Loan Officers</h2>
  <svg class="abs" style="left:140px;top:134px" width="12" height="18" viewBox="0 0 12 18"><path d="M9 2 L3 9 L9 16" fill="none" stroke="#fff" stroke-width="1.6"/></svg>
  <svg class="abs" style="left:1046px;top:134px" width="12" height="18" viewBox="0 0 12 18"><path d="M3 2 L9 9 L3 16" fill="none" stroke="#f47a1f" stroke-width="1.6"/></svg>
  <div class="partner" style="left:210px"><i></i>Northwind Crest</div>
  <div class="partner" style="left:380px"><i></i>Pinevale Home</div>
  <div class="partner" style="left:538px"><i></i>Summit Ridge</div>
  <div class="partner" style="left:716px"><i style="width:86px;height:52px;border-radius:4px;margin-top:-16px"></i></div>
  <div class="partner" style="left:868px;font-size:18px">Brightpath</div>
</section>

<!-- Testimonials -->
<section class="testimonials" role="img" aria-label="Blue-tinted photo of hands typing on a laptop keyboard">
  <h2 class="h2 serif" style="top:48px;color:var(--white)">Happy customers say</h2>
  <p class="abs" style="left:0;top:100px;width:1200px;text-align:center;font-family:'Lora',serif;font-size:34px;color:var(--white);line-height:34px">“</p>
  <p class="quote">"Sed ut perspiciatis unde omnis iste natus error sit voluptatem accusantium doloremque laudantium, totam rem aperiam, eaque ipsa quae ab illo inventore veritatis et quasi architecto beatae vitae dicta."</p>
  <p class="abs" style="left:0;top:266px;width:1200px;text-align:center;font-size:11px;color:var(--white)">Marlow Finch</p>
  <p class="abs" style="left:0;top:282px;width:1200px;text-align:center;font-size:8.5px;color:rgba(255,255,255,.8)">Lorem Ipsum</p>
  <svg class="abs" style="left:554px;top:300px" width="92" height="14" viewBox="0 0 92 14">
    <g fill="none" stroke="#fff"><circle cx="7" cy="7" r="5"/><circle cx="22" cy="7" r="5"/><circle cx="37" cy="7" r="5"/><circle cx="52" cy="7" r="5"/><circle cx="67" cy="7" r="5"/><circle cx="82" cy="7" r="5"/></g>
    <circle cx="22" cy="7" r="2.5" fill="#fff"/>
  </svg>
  <svg class="abs" style="left:0;top:420px" width="1200" height="200" viewBox="0 0 1200 200" preserveAspectRatio="none">
    <path d="M0 120 C250 40 420 160 640 110 S1000 20 1200 80 L1200 200 L0 200 Z" fill="rgba(255,255,255,.35)"/>
    <path d="M0 170 C260 100 480 200 720 150 S1050 90 1200 130 L1200 200 L0 200 Z" fill="#fff"/>
  </svg>
</section>

<!-- News -->
<h2 class="h2 serif" style="top:3250px">Latest news</h2>
<p class="lead" style="left:300px;top:3294px;width:600px;font-size:10.5px;line-height:19px">Lorem Ipsum is simply dummy text of the printing and typesetting industry. Lorem Ipsum has been the industry's standard dummy text ever since the 1500s, when an unknown</p>

<article class="news-card" style="left:200px">
  <div class="news-img" role="img" aria-label="Photo of a person holding a phone beside a cup of coffee" style="background:linear-gradient(135deg,#6b5646,#c9b7a4)"></div>
  <div class="news-box"><span class="news-badge"></span><p class="date">11 DEC 2021</p><h5>Lorem Ipsum is simply dummy text of the printing and typese industrys standard</h5></div>
</article>
<article class="news-card" style="left:475px">
  <div class="news-img" role="img" aria-label="Photo looking up between glass office towers into the sky" style="background:linear-gradient(180deg,#8fb7df,#35506f)"></div>
  <div class="news-box"><span class="news-badge"></span><p class="date">10 JAN 2022</p><h5>Lorem Ipsum is simply dummy text of the printing and typese industrys standard</h5></div>
</article>
<article class="news-card" style="left:750px">
  <div class="news-img" role="img" aria-label="Photo of colleagues reviewing work together at a laptop" style="background:linear-gradient(135deg,#2c2f38,#a9adb6)"></div>
  <div class="news-box"><span class="news-badge"></span><p class="date">15 MAR 2022</p><h5>Lorem Ipsum is simply dummy text of the printing and typese industrys standard</h5></div>
</article>
<div class="btn btn-blue" style="left:549px;top:3627px;width:100px;height:30px">View All</div>

<!-- CTA -->
<section class="cta">
  <h2 class="abs serif" style="left:48px;top:30px;font-size:26px;color:var(--white)">Best solution for your business.</h2>
  <div class="btn btn-orange" style="left:606px;top:31px;width:137px;height:28px">Get Started Today!</div>
</section>

<!-- Footer -->
<footer>
  <div class="abs brand" style="left:200px;top:3880px;font-size:22px"><span class="brand-dot"></span>Codewell Harbor</div>

  <h6 class="foot-h" style="left:406px">Contact Us</h6>
  <div class="contact-line" style="top:3900px;font-size:13px"><svg width="12" height="14" viewBox="0 0 12 14"><path d="M3 1 l2 3 l-1.5 1.5 c1 2 2 3 4 4 L9 8 l3 2 l-1 3 C6 13 0 7 1 2 Z" fill="#1b7fd6"/></svg>(555) 014-2288</div>
  <div class="contact-line" style="top:3928px"><svg width="12" height="12" viewBox="0 0 12 12"><rect x="0.5" y="2" width="11" height="8" rx="1" fill="#1b7fd6"/><path d="M1 3 l5 4 l5 -4" fill="none" stroke="#fff"/></svg>hello@codewellharbor.com</div>
  <div class="contact-line" style="top:3952px;font-size:9.5px;line-height:15px"><svg width="12" height="14" viewBox="0 0 12 14"><path d="M6 13 C2 8 1 6 1 5 a5 5 0 0 1 10 0 c0 1 -1 3 -5 8Z" fill="#1b7fd6"/><circle cx="6" cy="5" r="1.8" fill="#fff"/></svg><span>218 Harbor Lane, Suite 40, Riverton,<br>WA 98012</span></div>

  <h6 class="foot-h" style="left:642px">Quick Links</h6>
  <ul class="foot-list" style="left:642px">
    <li>Home</li><li>About</li><li>Products</li><li>Why Us?</li><li>News</li><li>Partners</li><li>Reviews</li><li>Contact Us</li>
  </ul>

  <h6 class="foot-h" style="left:793px">Products</h6>
  <ul class="foot-list" style="left:793px">
    <li>Applicant Harbor</li><li>Lending Harbor</li><li>Dwelling Harbor</li>
  </ul>

  <span class="social" style="top:3878px"></span>
  <span class="social" style="top:3915px;background:var(--orange)"></span>
  <span class="social" style="top:3952px"></span>
  <span class="social" style="top:3989px"></span>

  <p class="copyright">© 2022 Codewell Harbor. All Rights Reserved &nbsp;&nbsp; | &nbsp;&nbsp; Terms and Conditions &nbsp;&nbsp; | &nbsp;&nbsp; Privacy Policy</p>
</footer>

</body>
</html>
```